Help keep hoosiers happy and at home!

We need a billboard designed for our Indiana based healthcare business called 'Harbor Lane Home Aides'. We administer a medicaid waiver program that provides support and financial aid to live in caregivers that take care of someone who would otherwise be in a nursing home or skilled nursing facility. Qualified caregivers could be eligible to receive up to 1200 dollars a month in tax free financial aid, as well as access to nursing support that helps manage any unexpected situations or changes in a care recipients condition or care routine. Our program empowers families to keep their loved ones at home and out of the nursing home. NOTE: We believe the tagline at the bottom of our logo is disproportionately small. We would like to see that tagline larger and easier to read. I look forward to seeing your design ideas!

Target Market(s)

Medicaid aged beneficiaries and caregivers.

Industry/Entity Type

Home Healthcare

Colors
0054AA
0677BA
7BADD7
CADEEF
E8F1F8

Requirements
Nice to have
• "Empowering friends and family to care for their loves ones at home. Eligible participants receive up to $15,000 a year, tax free."

```html
<!DOCTYPE html>
<html lang="en">
<head>
<meta charset="utf-8">
<title>Harbor Lane Home Aides Billboard</title>
<link href="https://fonts.googleapis.com/css2?family=Poppins:wght@400;500;600;700;800&family=Oswald:wght@600&display=swap" rel="stylesheet">
<style>
  :root {
    --navy: #202f7c;
    --mid-blue: #4b8fcb;
    --light-blue: #7badd7;
    --pale: #e8ecf4;
    --red: #e3141b;
    --white: #ffffff;
    --ink: #222633;
    --page: #ffffff;
  }
  html, body {
    margin: 0;
    padding: 0;
    width: 970px;
    height: 1200px;
    overflow: hidden;
    background: var(--page);
  }
  .canvas {
    position: relative;
    width: 970px;
    height: 1200px;
  }
  .billboard {
    position: absolute;
    left: 20px;
    top: 406px;
    width: 930px;
    height: 388px;
    overflow: hidden;
    background: linear-gradient(180deg, var(--white) 0%, #f3f4f8 45%, #e6e8f0 100%);
    box-shadow: 0 4px 12px rgba(0,0,0,0.25);
    font-family: "Poppins", sans-serif;
  }
  .art {
    position: absolute;
    inset: 0;
  }
  .brand {
    position: absolute;
    left: 24px;
    top: 56px;
    width: 150px;
    display: flex;
    flex-direction: column;
    align-items: center;
    gap: 10px;
  }
  .brand-dot {
    width: 54px;
    height: 54px;
    border-radius: 50%;
    background: var(--navy);
  }
  .brand-name {
    color: var(--navy);
    font-weight: 600;
    font-size: 15px;
    line-height: 1.2;
    text-align: center;
  }
  .headline {
    position: absolute;
    left: 182px;
    top: 36px;
    margin: 0;
    color: var(--navy);
    font-weight: 800;
    font-size: 46px;
    line-height: 1;
    letter-spacing: 0.5px;
  }
  .subhead {
    position: absolute;
    left: 182px;
    top: 80px;
    margin: 0;
    color: var(--mid-blue);
    font-weight: 800;
    font-size: 31px;
    line-height: 1;
  }
  .tagline {
    position: absolute;
    left: 182px;
    top: 114px;
    width: 343px;
    height: 26px;
    background: var(--navy);
    color: var(--white);
    font-weight: 600;
    font-size: 15px;
    line-height: 26px;
    text-align: center;
    box-shadow: 0 4px 0 #9aa0b4;
    margin: 0;
  }
  .offer-band {
    position: absolute;
    left: 0;
    top: 168px;
    width: 520px;
    height: 101px;
    background: linear-gradient(90deg, var(--mid-blue) 0%, var(--mid-blue) 48%, #9fb2d8 85%, rgba(200,205,225,0.6) 100%);
  }
  .offer-label {
    position: absolute;
    left: 40px;
    top: 175px;
    margin: 0;
    font-weight: 800;
    font-size: 23px;
    line-height: 31px;
    color: var(--white);
  }
  .offer-label .lead { color: var(--navy); }
  .offer-divider {
    position: absolute;
    left: 252px;
    top: 178px;
    height: 82px;
    border-left: 2px dotted rgba(255,255,255,0.85);
  }
  .offer-amount {
    position: absolute;
    left: 266px;
    top: 168px;
    margin: 0;
    font-family: "Oswald", sans-serif;
    font-weight: 600;
    font-size: 52px;
    line-height: 1.1;
    color: var(--red);
  }
  .offer-period {
    position: absolute;
    left: 267px;
    top: 230px;
    margin: 0;
    font-weight: 700;
    font-size: 24px;
    line-height: 1;
    color: var(--navy);
  }
  .badge-text {
    position: absolute;
    left: 425px;
    top: 208px;
    width: 132px;
    margin: 0;
    text-align: center;
    color: var(--white);
    font-weight: 800;
    font-size: 38px;
    line-height: 36px;
  }
  .visit {
    position: absolute;
    left: 44px;
    top: 284px;
    margin: 0;
    color: var(--ink);
    font-weight: 500;
    font-size: 15px;
  }
  .url {
    position: absolute;
    left: 46px;
    top: 325px;
    margin: 0;
    color: var(--white);
    font-weight: 600;
    font-size: 18px;
    letter-spacing: 3px;
  }
</style>
</head>
<body>
<main class="canvas">
  <section class="billboard">
    <svg class="art" width="930" height="388" viewBox="0 0 930 388" aria-hidden="false">
      <defs>
        <linearGradient id="photoTone" x1="0" y1="0" x2="1" y2="1">
          <stop offset="0" stop-color="#8a4a2a"/>
          <stop offset="0.45" stop-color="#a85a44"/>
          <stop offset="0.75" stop-color="#6f7ea0"/>
          <stop offset="1" stop-color="#b83a2c"/>
        </linearGradient>
      </defs>
      <!-- bottom navy band -->
      <polygon class="url-band" points="0,310 534,310 563,388 0,388" fill="var(--navy)"/>
      <!-- curved accent stripe -->
      <path class="accent-arc" d="M598,0 L930,0 L930,388 L630,388 C545,330 515,230 530,150 C545,80 570,30 598,0 Z" fill="var(--mid-blue)"/>
      <path class="accent-gap" d="M640,0 L930,0 L930,388 L652,388 C575,330 548,240 556,165 C563,95 600,35 640,0 Z" fill="var(--white)"/>
      <!-- photo area -->
      <path class="photo" role="img" aria-label="Photo: a smiling young caregiver standing behind an older man in a wheelchair outside a brick home" d="M646,0 L930,0 L930,388 L660,388 C585,330 560,240 566,165 C573,98 606,36 646,0 Z" fill="url(#photoTone)"/>
      <!-- tax free badge -->
      <circle class="badge-ring" cx="486" cy="245" r="68" fill="var(--navy)"/>
      <circle class="badge-edge" cx="491" cy="254" r="68" fill="var(--white)"/>
      <circle class="badge" cx="491" cy="254" r="64" fill="var(--mid-blue)"/>
    </svg>

    <div class="brand">
      <span class="brand-dot"></span>
      <span class="brand-name">Harbor Lane Home Aides</span>
    </div>

    <h1 class="headline">EMPOWERING</h1>
    <h2 class="subhead">FRIENDS &amp; FAMILY</h2>
    <p class="tagline">TO CARE FOR THEIR LOVES ONES AT HOME</p>

    <div class="offer-band"></div>
    <p class="offer-label"><span class="lead">ELIGIBLE</span><br>PARTICIPANTS<br>RECEIVE UP TO</p>
    <div class="offer-divider"></div>
    <p class="offer-amount">$15,000</p>
    <p class="offer-period">A YEAR</p>
    <p class="badge-text">TAX<br>FREE</p>

    <p class="visit">Visit our website for more information</p>
    <p class="url">WWW.HARBORLANEHOMEAIDES.COM</p>
  </section>
</main>
</body>
</html>
```